MEDICAL CLINIC LETTERHEAD

Design is a letterhead for a non-profit medical center. The name of the clinic is VITORRANE Community Health Center. Although the full name must be included, the community health center part is more of a description and should be less visible - i attached an example of what I mean by that (ATTACHED IMAGE IS AN EXAMPLE OF FONT SIZES NOT A DESIGN IDEA). Please design something modern, cool looking and unique because I can always download free templates.
Phone, email, website and etc will be added later.

Industry/Entity Type

MEDICAL

```html
<!DOCTYPE html>
<html lang="en">
<head>
<meta charset="utf-8">
<title>VITORRANE Community Health Center – Letterhead</title>
<link rel="stylesheet" href="https://fonts.googleapis.com/css2?family=Montserrat:wght@600&family=Source+Sans+3:wght@400&display=swap">
<style>
  :root {
    --navy: #0b2f5b;
    --sky: #29abe2;
    --paper: #ffffff;
    --body-grey: #8a8d91;
    --ink: #333638;
    --rule: #6f7275;
  }
  * { margin: 0; padding: 0; box-sizing: border-box; }
  html, body { width: 960px; height: 1200px; overflow: hidden; background: var(--paper); }
  .letterhead {
    position: relative;
    width: 960px;
    height: 1200px;
    background: var(--paper);
    font-family: "Source Sans 3", "Myriad Pro", sans-serif;
  }
  .brand {
    position: absolute;
    top: 58px;
    left: 0;
    width: 100%;
    text-align: center;
    color: var(--navy);
    font-family: "Montserrat", sans-serif;
    font-weight: 600;
  }
  .brand-mark {
    display: block;
    width: 58px;
    height: 58px;
    margin: 0 auto 24px;
    background: var(--sky);
  }
  .brand-name {
    display: block;
    font-size: 31px;
    letter-spacing: 1px;
    line-height: 1;
  }
  .brand-descriptor {
    display: block;
    margin-top: 6px;
    font-size: 12px;
    letter-spacing: 0.6px;
    line-height: 1;
  }
  .salutation {
    position: absolute;
    top: 308px;
    left: 81px;
    font-size: 17px;
    color: var(--body-grey);
  }
  .letter-body {
    position: absolute;
    top: 384px;
    left: 61px;
    width: 838px;
    font-size: 16.6px;
    line-height: 21.8px;
    color: var(--body-grey);
    text-align: justify;
  }
  .letter-body p + p { margin-top: 21.8px; }
  .letter-body p.opening { text-indent: 56px; }
  .contact-bar {
    position: absolute;
    top: 1087px;
    left: 0;
    width: 100%;
    height: 56px;
    font-size: 15px;
    line-height: 19px;
    color: var(--ink);
  }
  .contact-item {
    position: absolute;
    display: flex;
    gap: 8px;
  }
  .contact-item svg { flex: none; margin-top: 2px; }
  .contact-address { left: 62px; top: 12px; }
  .contact-phones { left: 441px; top: 4px; }
  .contact-web { left: 722px; top: 4px; }
  .contact-lines { display: flex; flex-direction: column; gap: 4px; }
  .contact-lines span { display: flex; align-items: center; gap: 8px; }
  .divider {
    position: absolute;
    top: 0;
    width: 1px;
    height: 56px;
    background: var(--rule);
  }
  .divider-1 { left: 338px; }
  .divider-2 { left: 657px; }
  .footer-band { position: absolute; left: 0; bottom: 0; width: 960px; height: 44px; }
</style>
</head>
<body>
<main class="letterhead">
  <header class="brand">
    <span class="brand-mark" aria-hidden="true"></span>
    <span class="brand-name">VITORRANE</span>
    <span class="brand-descriptor">COMMUNITY HEALTH CENTER</span>
  </header>

  <p class="salutation">Dear Sir</p>

  <section class="letter-body">
    <p class="opening">Lorem ipsum dolor sit amet, consectetur adipiscing elit. Integer eu odio mattis, pulvinar turpis quis, faucibus nisl. Proin feugiat, erat vitae cursus pharetra, enim est semper ligula, in malesuada orci nisl et diam. Etiam elementum metus ac fringilla vulputate. Etiam mattis ligula sed ante mollis bibendum. Orci varius natoque penatibus et magnis dis parturient montes, nascetur ridiculus mus.</p>
    <p>Ut nibh augue, blandit ac orci ac, rutrum congue enim. Suspendisse gravida vulputate felis, quis interdum orci tincidunt quis. Praesent imperdiet maximus neque. Mauris ut dui enim. Nullam at efficitur elit. Donec ante ipsum, fermentum at lectus vel, blandit vulputate ante. Proin luctus suscipit diam id vestibulum. Morbi malesuada id mauris eget ullamcorper.</p>
    <p>Donec varius orci purus, vitae aliquam libero volutpat id. Integer sed imperdiet libero. Aliquam accumsan, risus sit amet ornare consectetur, turpis felis dictum justo, non rhoncus mauris dui sed velit. Pellentesque habitant morbi tristique senectus et netus et malesuada fames ac turpis egestas. Pellentesque tincidunt vitae ligula nec imperdiet. Donec sed congue enim. Nullam elementum faucibus nulla nec vestibulum. Sed at tempor ligula. In quis vulputate nunc. Integer at gravida lacus, ac tristique risus. Sed at vulputate nulla.</p>
    <p>Praesent blandit nunc eu efficitur commodo. In tempor nisi ex, vel venenatis ante vestibulum a. Duis vestibulum nibh a erat sagittis, nec euismod lorem varius. Nam ultricies turpis sed justo sollicitudin volutpat. Morbi sed mollis eros. Sed quis tortor id enim vehicula porttitor. Curabitur non aliquam ex. Phasellus dignissim fermentum elit, at finibus ligula mattis eget.</p>
  </section>

  <footer class="contact-bar">
    <div class="contact-item contact-address">
      <svg width="12" height="17" viewBox="0 0 12 17" aria-hidden="true">
        <path d="M6 1a5 5 0 0 0-5 5c0 3.6 5 10 5 10s5-6.4 5-10a5 5 0 0 0-5-5z" fill="none" stroke="#444" stroke-width="1.6"/>
        <circle cx="6" cy="6" r="1.8" fill="#444"/>
      </svg>
      <div class="contact-lines" style="gap:0">
        <span>suit # 00, Lorem ipsum</span>
        <span>Lorem Lorem ipsum</span>
      </div>
    </div>
    <div class="divider divider-1"></div>
    <div class="contact-item contact-phones">
      <div class="contact-lines">
        <span><svg width="12" height="12" viewBox="0 0 12 12" aria-hidden="true"><path d="M2.5 1l2 2.3-1 1.2a7 7 0 0 0 4 4l1.2-1 2.3 2-1.2 1.5C5.6 11 1 6.4 1 2.2z" fill="#444"/></svg>000-000-0000</span>
        <span><svg width="12" height="12" viewBox="0 0 12 12" aria-hidden="true"><path d="M2.5 1l2 2.3-1 1.2a7 7 0 0 0 4 4l1.2-1 2.3 2-1.2 1.5C5.6 11 1 6.4 1 2.2z" fill="#444"/></svg>000-000-0000</span>
      </div>
    </div>
    <div class="divider divider-2"></div>
    <div class="contact-item contact-web">
      <div class="contact-lines" style="gap:0">
        <span><svg width="14" height="12" viewBox="0 0 14 12" aria-hidden="true"><path d="M1 5l6-4 6 4v6H1z" fill="#444"/><path d="M1 5l6 4 6-4" fill="none" stroke="#fff" stroke-width="1.2"/></svg>info@VITORRANE.com</span>
        <span><svg width="14" height="14" viewBox="0 0 14 14" aria-hidden="true"><g fill="none" stroke="#444" stroke-width="1.1"><circle cx="7" cy="7" r="5.5"/><ellipse cx="7" cy="7" rx="2.4" ry="5.5"/><path d="M1.5 7h11M2.5 4h9M2.5 10h9"/></g></svg>www.VITORRANE.com</span>
      </div>
    </div>
  </footer>

  <svg class="footer-band" viewBox="0 0 960 44" aria-hidden="true">
    <rect x="0" y="0" width="960" height="44" fill="var(--sky)"/>
    <polygon points="0,0 490,0 446,44 0,44" fill="var(--navy)"/>
    <polygon points="490,0 496,0 452,44 446,44" fill="#ffffff"/>
  </svg>
</main>
</body>
</html>
```